Business Card for Business consulting practice

Need a design for a consultant business card. Simple and elegant.
I need the following information on the card:
Logo: (see uploaded file)
Company name: Calmora Advisory Group
Name: Dana Weltrup
Title: Managing Director - Aerospace and Defence
Phone #: 514-268-3917
e-mail: dana.weltrup@calmora-example.com
Website: www.calmora-example.com
Tagline: Proposals Management and Capture support for complex procurements

```html
<!DOCTYPE html>
<html lang="en">
<head>
<meta charset="utf-8">
<title>Calmora Advisory Group – Business Card</title>
<link rel="stylesheet" href="https://fonts.googleapis.com/css2?family=Cinzel:wght@700&family=Roboto+Condensed:wght@400&family=Raleway:wght@400;500&display=swap">
<style>
  :root {
    --navy: #0b2a42;
    --navy-deep: #082235;
    --accent: #1a9ad0;
    --accent-bright: #2fc4f0;
    --ink: #0b2a42;
    --text-grey: #333b42;
    --paper: #ffffff;
    --backdrop: #d9d9db;
  }
  * { box-sizing: border-box; margin: 0; padding: 0; }
  html, body { width: 1200px; height: 900px; overflow: hidden; }
  body {
    background: var(--backdrop);
    display: flex;
    flex-direction: column;
    align-items: center;
    justify-content: center;
    gap: 40px;
  }
  .card {
    width: 700px;
    height: 400px;
    position: relative;
    overflow: hidden;
    box-shadow: 0 10px 30px rgba(0,0,0,0.18);
  }

  /* Back side */
  .card-back { background: var(--navy-deep); }
  .card-back .pattern-field {
    position: absolute; inset: 0;
    background: linear-gradient(100deg, var(--accent-bright) 0%, #1b7fb0 25%, var(--navy) 60%, var(--navy-deep) 100%);
  }
  .card-back .back-brand {
    position: absolute; right: 40px; bottom: 140px;
    display: flex; align-items: center; gap: 10px;
    font-family: "Cinzel", serif; font-weight: 700; font-size: 20px;
    color: var(--paper); letter-spacing: 1px;
  }
  .brand-dot {
    width: 14px; height: 14px; border-radius: 50%;
    background: var(--paper);
  }

  /* Front side */
  .card-front { background: var(--paper); }
  .brand {
    position: absolute; left: 40px; top: 150px; width: 280px;
    text-align: center;
    font-family: "Cinzel", serif; font-weight: 700;
    font-size: 26px; line-height: 1.15;
    color: var(--ink); letter-spacing: 1px;
  }
  .divider {
    position: absolute; left: 345px; top: 60px;
    width: 1px; height: 180px;
    background: linear-gradient(to bottom, transparent, #c9ced3 20%, #c9ced3 80%, transparent);
  }
  .contact-block { position: absolute; left: 372px; top: 78px; }
  .person-name {
    font-family: "Cinzel", serif; font-weight: 700;
    font-size: 26px; color: var(--ink); letter-spacing: 1px;
  }
  .person-title {
    font-family: "Roboto Condensed", sans-serif;
    font-size: 15px; color: var(--accent); margin-top: 2px;
  }
  .contact-list { list-style: none; margin-top: 16px; }
  .contact-list li {
    display: flex; align-items: center; gap: 8px;
    font-family: "Raleway", sans-serif; font-size: 14px;
    color: var(--text-grey); line-height: 22px;
  }
  .contact-list svg { width: 12px; height: 12px; fill: var(--ink); flex-shrink: 0; }
  .tagline-band {
    position: absolute; left: 0; right: 0; top: 300px; height: 50px;
    background: var(--navy);
    display: flex; align-items: center; justify-content: center;
    font-family: "Raleway", sans-serif; font-weight: 500;
    font-size: 16px; color: var(--paper); letter-spacing: 0.3px;
  }
</style>
</head>
<body>

  <section class="card card-back">
    <div class="pattern-field" role="img" aria-label="Repeating brand emblem pattern fading from bright blue to deep navy"></div>
    <div class="back-brand"><span class="brand-dot"></span>Calmora</div>
  </section>

  <section class="card card-front">
    <div class="brand">Calmora Advisory Group</div>
    <div class="divider"></div>
    <div class="contact-block">
      <h1 class="person-name">Dana Weltrup</h1>
      <p class="person-title">Managing Director/ Aerospace &amp; Defence</p>
      <ul class="contact-list">
        <li>
          <svg viewBox="0 0 24 24" aria-hidden="true"><path d="M6.6 10.8a15.1 15.1 0 0 0 6.6 6.6l2.2-2.2a1 1 0 0 1 1-.25 11.4 11.4 0 0 0 3.6.57 1 1 0 0 1 1 1V20a1 1 0 0 1-1 1A17 17 0 0 1 3 4a1 1 0 0 1 1-1h3.5a1 1 0 0 1 1 1c0 1.25.2 2.45.57 3.57a1 1 0 0 1-.25 1z"/></svg>
          514-268-3917
        </li>
        <li>
          <svg viewBox="0 0 24 24" aria-hidden="true"><path d="M2 5h20v14H2z M2 5l10 8 10-8" /></svg>
          dana.weltrup@calmora-example.com
        </li>
        <li>
          <svg viewBox="0 0 24 24" aria-hidden="true"><circle cx="12" cy="12" r="10"/></svg>
          www.calmora-example.com
        </li>
      </ul>
    </div>
    <div class="tagline-band">Proposals Management &amp; Capture support for complex procurements</div>
  </section>

</body>
</html>
```